A Speech Therapy Business needs to update their logo

I need an update to the font and color of my logo to look more appealing. I am looking to open a private practice as a Speech Language Pathologist that caters to adults and children. It needs to be sophisticated and friendly at the same time. I want to keep the silhouette in my logo as is, just update the font and color for "Brightpath".
Industry/Entity Type
Business
Contact Information for Business Card
I want the business card to have my logo, my name (Odile Varn, CCC-SLP, TSSLD) and that I am a Bilingual Speech Language Pathologist. Also, include my phone number, (718) 555-0193. Include my website, Brightpathslp.example, and email address, odilevarn@brightpathslp.example
Look and feel

```html
<!DOCTYPE html>
<html lang="en">
<head>
<meta charset="utf-8">
<title>Brightpath – Logo and Business Card</title>
<link rel="stylesheet" href="https://fonts.googleapis.com/css2?family=Oswald:wght@600&family=Open+Sans:wght@400;600&family=PT+Sans+Narrow:wght@400&display=swap">
<style>
  :root {
    --page-bg: #d8d9db;
    --card-white: #ffffff;
    --card-grey-light: #f7f8f9;
    --card-grey: #dcdee1;
    --brand-blue: #0f5f94;
    --brand-slate: #3a5266;
    --figure-grey: #5f6b74;
    --text-dark: #333333;
    --rule: #9a9ea3;
  }
  * { margin: 0; padding: 0; box-sizing: border-box; }
  html, body {
    width: 1200px; height: 1200px; overflow: hidden;
    background: var(--page-bg);
  }
  .canvas { position: relative; width: 1200px; height: 1200px; }

  .card {
    position: absolute; left: 216px; width: 770px; height: 480px; overflow: hidden;
  }

  /* Logo card */
  .logo-card { top: 64px; background: var(--card-white); }
  .logo-card .figures {
    position: absolute; left: 68px; top: 20px; width: 644px; height: 270px;
    background: linear-gradient(100deg, var(--figure-grey) 0%, #76818a 100%);
    clip-path: polygon(0 0, 30% 0, 100% 70%, 100% 100%, 0 100%);
    opacity: .85;
  }
  .logo-card .wordmark {
    position: absolute; left: 68px; top: 282px;
    font-family: "Oswald", sans-serif; font-weight: 600;
    font-size: 150px; line-height: 1; color: var(--brand-blue);
    letter-spacing: -1px;
  }

  /* Business card */
  .business-card {
    top: 608px;
    background: radial-gradient(ellipse at 50% 8%, var(--card-grey-light) 0%, #eceef0 45%, var(--card-grey) 100%);
  }
  .business-card .top-tab {
    position: absolute; left: 136px; top: 0; width: 500px; height: 7px;
    background: var(--brand-blue); border-radius: 0 0 8px 8px;
  }
  .business-card .figures {
    position: absolute; left: 288px; top: 30px; width: 208px; height: 88px;
    background: linear-gradient(100deg, var(--figure-grey) 0%, #76818a 100%);
    clip-path: polygon(0 0, 30% 0, 100% 70%, 100% 100%, 0 100%);
    opacity: .85;
  }
  .business-card .wordmark {
    position: absolute; left: 288px; top: 112px;
    font-family: "Oswald", sans-serif; font-weight: 600;
    font-size: 48px; line-height: 1.1; color: var(--brand-blue);
  }
  .business-card .divider {
    position: absolute; left: 258px; top: 184px; width: 258px; height: 1px;
    background: var(--rule);
  }
  .business-card .name {
    position: absolute; left: 0; right: 0; top: 204px; text-align: center;
    font-family: "Open Sans", sans-serif; font-weight: 400;
    font-size: 46px; line-height: 1.2; color: var(--text-dark);
  }
  .business-card .title {
    position: absolute; left: 0; right: 0; top: 264px; text-align: center;
    font-family: "Open Sans", sans-serif; font-weight: 600;
    font-size: 19px; color: var(--brand-blue);
  }
  .contact {
    position: absolute; left: 517px; top: 358px; padding-left: 16px;
    border-left: 1px solid var(--rule); list-style: none;
  }
  .contact li {
    display: flex; align-items: center; height: 34px;
    font-family: "PT Sans Narrow", sans-serif; font-size: 16px; color: var(--text-dark);
  }
  .contact .icon {
    width: 18px; height: 18px; margin-right: 6px; flex: none;
    color: var(--brand-slate); fill: none; stroke: currentColor; stroke-width: 1.8;
  }
  .contact .at {
    width: 18px; margin-right: 6px; text-align: center;
    font-family: "Open Sans", sans-serif; font-weight: 600; font-size: 17px; color: var(--brand-slate);
  }
  .bottom-bands { position: absolute; left: 0; bottom: 0; width: 770px; height: 24px; }
</style>
</head>
<body>
<main class="canvas">

  <section class="card logo-card">
    <div class="figures" role="img" aria-label="Silhouettes of a family walking hand in hand, from adult down to toddler, ending with a small heart"></div>
    <div class="wordmark">Brightpath</div>
  </section>

  <section class="card business-card">
    <div class="top-tab"></div>
    <div class="figures" role="img" aria-label="Small silhouettes of a family walking hand in hand, ending with a heart"></div>
    <div class="wordmark">Brightpath</div>
    <div class="divider"></div>
    <h1 class="name">Odile Varn</h1>
    <p class="title">Bilingual Speech Language Pathologist</p>

    <ul class="contact">
      <li>
        <svg class="icon" viewBox="0 0 24 24" aria-hidden="true"><path fill="currentColor" stroke="none" d="M6.6 2.5c.6-.4 1.4-.2 1.8.4l2 3.3c.3.6.2 1.3-.3 1.7l-1.5 1.2c.9 2.3 2.5 4.2 4.6 5.6l1.3-1.4c.5-.5 1.2-.6 1.8-.2l3.2 2.1c.6.4.8 1.2.4 1.8l-1.3 2.2c-.5.8-1.5 1.2-2.4.9C9.5 18.3 4.9 12.8 4 6.1c-.1-.9.3-1.8 1.1-2.3z"/></svg>
        (718) 555-0193
      </li>
      <li>
        <svg class="icon" viewBox="0 0 24 24" aria-hidden="true"><circle cx="12" cy="12" r="9"/><ellipse cx="12" cy="12" rx="4" ry="9"/><path d="M3 12h18M4.5 7.5h15M4.5 16.5h15"/></svg>
        odilevarn@brightpathslp.example
      </li>
      <li>
        <span class="at" aria-hidden="true">@</span>
        Brightpathslp.example
      </li>
    </ul>

    <svg class="bottom-bands" viewBox="0 0 770 24" aria-hidden="true">
      <polygon points="0,2 496,2 488,24 0,24" fill="#3a5266"/>
      <path d="M522,0 H770 V24 H504 C506,10 512,0 522,0 Z" fill="#0f5f94"/>
    </svg>
  </section>

</main>
</body>
</html>
```